Ironvale Holdings Business card

We need a an amazing matte black and gold card! W are a finance investing company so we want something that's eye catching and sleek. We want it to be attractive and sleek and represent money. Heck with would like the letters and lgo to be printed as 24k gold one day. We have the logo added so please use the color scheme with the logo and have that beautifully placed on one side.

Target Market(s)

Investors of all ages

Industry/Entity Type

Financial

Contact Information for Business Card

Black and matte with gold lettering follow logo colrs please.

Font styles to use
Other font styles liked:
• you decide

Colors

Designer to choose colors to be used in the design.

Requirements
Must have
• Matte Black and Gold, logo on one side. job title and name , website, phone number and email address on the other side
Nice to have
• Matte black and crisp finish to attract investors
Should not have
• playful, very professional!

```html
<!DOCTYPE html>
<html lang="en">
<head>
<meta charset="utf-8">
<title>Ironvale Holdings – Business Card</title>
<link href="https://fonts.googleapis.com/css2?family=Montserrat:wght@400;600;700&family=Lato:wght@400&display=swap" rel="stylesheet">
<style>
  :root {
    --backdrop: #e9e6e1;
    --charcoal: #302d2e;
    --black: #050505;
    --gold-yellow: #e8d55a;
    --gold-metal: #c9a52a;
    --white: #ffffff;
    --ink: #111111;
  }
  * { margin: 0; padding: 0; box-sizing: border-box; }
  html, body { width: 1200px; height: 892px; overflow: hidden; background: var(--backdrop); }
  .canvas {
    position: relative; width: 1200px; height: 892px;
    display: flex; align-items: center; justify-content: center; gap: 40px;
  }
  .card {
    position: relative; width: 540px; height: 309px; overflow: hidden;
    box-shadow: 0 10px 28px rgba(0,0,0,.25);
  }
  .card-shape { position: absolute; inset: 0; width: 100%; height: 100%; }

  /* Front – contact side */
  .card--front { background: var(--charcoal); }
  .brand {
    position: absolute; font-family: "Montserrat", sans-serif; font-weight: 600;
    text-transform: uppercase; text-align: center; line-height: 1.15;
  }
  .card--front .brand { left: 20px; top: 120px; width: 240px; color: var(--ink); font-size: 22px; letter-spacing: 2px; }
  .card--front .brand span { display: block; font-size: 14px; letter-spacing: 5px; }
  .person { position: absolute; left: 336px; top: 68px; font-family: "Montserrat", sans-serif; }
  .person-name { color: var(--white); font-weight: 700; font-size: 15px; letter-spacing: .4px; white-space: nowrap; }
  .person-title { color: var(--gold-yellow); font-size: 9px; font-weight: 400; margin-top: -1px; }
  .contact {
    position: absolute; font-family: "Lato", sans-serif; color: var(--white);
    font-size: 9.5px; letter-spacing: .8px; white-space: nowrap; line-height: 1.3;
  }

  /* Back – logo side */
  .card--back { background: var(--black); }
  .card--back .brand { left: 190px; top: 110px; width: 300px; color: var(--gold-metal); font-size: 28px; letter-spacing: 3px; }
  .card--back .brand span { display: block; font-size: 16px; letter-spacing: 9px; margin-top: 4px; }
  .back-web {
    position: absolute; left: 70px; top: 262px; display: flex; align-items: center; gap: 8px;
    font-family: "Lato", sans-serif; font-size: 12px; color: var(--ink); letter-spacing: .5px;
  }
</style>
</head>
<body>
<main class="canvas">

  <!-- Contact side -->
  <section class="card card--front">
    <svg class="card-shape" viewBox="0 0 540 309" aria-hidden="true">
      <path d="M0 0 H240 C350 40 350 270 230 309 H0 Z" fill="var(--gold-yellow)"/>
      <g fill="var(--charcoal)" stroke="var(--gold-yellow)" stroke-width="2.5">
        <circle cx="309" cy="80" r="13"/>
        <circle cx="318" cy="122" r="13"/>
        <circle cx="321" cy="164" r="13"/>
        <circle cx="314" cy="206" r="13"/>
        <circle cx="298" cy="248" r="13"/>
      </g>
      <!-- person -->
      <g transform="translate(309 80)" fill="var(--gold-yellow)">
        <circle cx="0" cy="-3" r="3.5"/>
        <path d="M-7 7 a7 5.5 0 0 1 14 0 Z"/>
      </g>
      <!-- phone -->
      <g transform="translate(318 122)" fill="var(--gold-yellow)">
        <path d="M-5 -6 q2-2 4 0 l2 3 q1 2-1 3 q1 4 5 6 q1-2 3-1 l3 2 q2 2 0 4 q-3 3-8 0 q-6-4-9-11 q-1-4 1-6 Z"/>
      </g>
      <!-- mail -->
      <g transform="translate(321 164)">
        <path d="M-7 -5 h14 v10 h-14 Z" fill="var(--gold-yellow)"/>
        <path d="M-7 -5 l7 5 l7-5" fill="none" stroke="var(--charcoal)" stroke-width="1.4"/>
      </g>
      <!-- globe -->
      <g transform="translate(314 206)" fill="none" stroke="var(--gold-yellow)" stroke-width="1.3">
        <circle cx="0" cy="0" r="6.5"/>
        <ellipse cx="0" cy="0" rx="2.8" ry="6.5"/>
        <path d="M-6.5 0 h13"/>
      </g>
      <!-- pin -->
      <g transform="translate(298 248)">
        <path d="M0 -7 a5.5 5.5 0 0 1 5.5 5.5 c0 4-5.5 9-5.5 9 s-5.5-5-5.5-9 a5.5 5.5 0 0 1 5.5-5.5 Z" fill="var(--gold-yellow)"/>
        <circle cx="0" cy="-1.5" r="2" fill="var(--charcoal)"/>
      </g>
    </svg>

    <div class="brand">Ironvale<span>Holdings</span></div>

    <div class="person">
      <div class="person-name">YOU FULL NAME</div>
      <div class="person-title">CEO</div>
    </div>
    <div class="contact" style="left:342px;top:116px">+012 345 6789 / +012 345 6789</div>
    <div class="contact" style="left:345px;top:158px">urname@email.com</div>
    <div class="contact" style="left:338px;top:200px">urwebsitename.com</div>
    <div class="contact" style="left:322px;top:236px">ur address goes here<br>street, zip code 0132</div>
  </section>

  <!-- Logo side -->
  <section class="card card--back">
    <svg class="card-shape" viewBox="0 0 540 309" aria-hidden="true">
      <path d="M0 205 C40 225 80 238 130 236 C180 234 200 218 250 222 C300 226 320 250 330 280 C336 298 340 309 345 309 H0 Z" fill="var(--gold-yellow)"/>
    </svg>

    <div class="brand">Ironvale<span>Holdings</span></div>

    <div class="back-web">
      <svg width="12" height="12" viewBox="0 0 12 12" aria-hidden="true">
        <g fill="none" stroke="var(--ink)" stroke-width="1">
          <circle cx="6" cy="6" r="5"/><ellipse cx="6" cy="6" rx="2.2" ry="5"/><path d="M1 6 h10"/>
        </g>
      </svg>
      <span>urwebsitename.com</span>
    </div>
  </section>

</main>
</body>
</html>
```